WP website design (FELM)

We need a wordpress design that will incorporate a professional color scheme with company logo in a clean layout. The design needs to consider that this will be developed on a responsive theme. Colors are undetermined - those that will complement the logo.
Client mentions liking brintonsale.example for the layout and use of color. Possible but not necessary to have large slideshow element.

Industry/Entity Type

It Company

Font styles to use
Sans Serif

Colors

Designer to choose colors to be used in the design.

Requirements
Must have
• - Navigation: 1)Home 2) Auctions 3) Services 4) About Us 5) FAQs 6) References 7) Contact Us

Site will have slideshow, please use high-end stock real estate image initially. Header will have logo. Social icons (Facebook, Twitter, Youtube)

Widgets Include: Email signup form, Featured Auctions, Featured Video widget.

Footer will have contact info (below), site navigation, smaller company logo, affiliation logos (attached).

FELM Auction Group
4172 Quill Ferry Lane
Paducah, KY 42917
1-800-555-BIDS (2437)
Ph. (270) 555-0148
Fx. (270) 555-0193
Nice to have
• - Site will have drop-down menus - please indicate the styling, for instance the dropdown menus 1) Live 2) Online 3) Past - under the 'Auctions' link

```html
<!DOCTYPE html>
<html lang="en">
<head>
<meta charset="utf-8">
<title>FELM Auction Group</title>
<link href="https://fonts.googleapis.com/css2?family=Open+Sans:wght@400;600;700&family=Arimo:wght@400;700&display=swap" rel="stylesheet">
<style>
:root{
  --red:#d0121a;
  --dark:#3d3d3d;
  --nav:#454545;
  --text:#555;
  --muted:#8a8a8a;
  --line:#d6d6d6;
  --panel:#f7f7f7;
  --footer:#4a4a4a;
}
*{box-sizing:border-box;margin:0;padding:0}
html,body{width:984px;height:1200px;overflow:hidden}
body{position:relative;font-family:"Arimo",Arial,sans-serif;color:var(--text);
  background:linear-gradient(#fff 0,#f3f3f3 330px,#e2e2e2 362px,#f5f5f5 440px,#fff 600px,#fff 100%)}
.abs{position:absolute}
.brand{left:130px;top:26px;display:flex;align-items:center;gap:8px;font-family:"Open Sans",sans-serif;font-weight:700;font-size:22px;color:var(--red);line-height:1}
.brand-mark{width:18px;height:18px;border-radius:50%;background:var(--red)}
.phone{left:707px;top:60px;display:flex;align-items:center;gap:6px;font-family:"Open Sans",sans-serif;font-weight:600;font-size:17px;color:var(--dark)}
.nav{left:123px;top:101px;width:739px;height:38px;background:var(--nav);border-radius:3px;display:flex;overflow:hidden}
.nav a{color:#fff;text-decoration:none;font-size:12px;display:flex;align-items:center;justify-content:center;border-right:1px solid #5a5a5a;letter-spacing:.2px}
.nav a:last-child{border-right:0}
.nav .home{background:var(--red);width:62px}
.slider{left:123px;top:147px;width:739px;height:267px;background:#fff;border:1px solid var(--line);border-radius:4px;box-shadow:0 8px 10px -8px rgba(0,0,0,.4)}
.slide-photo{left:4px;top:4px;width:731px;height:258px;border-radius:3px;
  background:linear-gradient(#7fb2e0 0%,#a9c6d8 18%,#5b4b44 30%,#6d5c53 45%,#e9e1d2 55%,#5c4a3d 75%,#4f7b2f 88%,#3f6a24 100%)}
.cap{left:35px;color:#fff;font-size:19px;padding:0 6px;display:flex;align-items:center}
.cap-1{top:153px;width:354px;height:37px;background:rgba(208,18,26,.9)}
.cap-2{top:191px;width:284px;height:36px;background:rgba(60,60,60,.75)}
.dots{left:36px;top:240px;display:flex;gap:4px}
.dots i{width:6px;height:6px;border-radius:50%;background:#fff}
.dots i:first-child{background:var(--red)}
.panel{background:linear-gradient(#fff,var(--panel));border:1px solid var(--line);border-radius:4px;box-shadow:0 2px 3px rgba(0,0,0,.12)}
.welcome{left:123px;top:437px;width:739px;height:149px;text-align:center;padding:14px 26px 0}
.welcome h1{font-family:"Open Sans",sans-serif;font-weight:700;font-size:20px;color:#555;margin-bottom:6px}
.welcome h1 span{color:var(--red)}
.welcome p{font-size:10.4px;line-height:14px;margin-bottom:6px;color:#666}
.more{color:var(--red)}
.h2{font-family:"Open Sans",sans-serif;font-weight:600;font-size:14.5px;color:#555}
.featured{left:123px;top:610px;width:739px;height:210px}
.featured .h2{position:absolute;left:14px;top:13px}
.arrow{position:absolute;color:#999;font-size:20px}
.item{position:absolute;top:36px;width:120px}
.thumb{width:115px;height:77px;background:#fff;padding:3px;border:1px solid #ddd;box-shadow:0 3px 4px rgba(0,0,0,.2)}
.thumb div{width:100%;height:100%}
.item h3{font-family:"Open Sans",sans-serif;font-weight:400;font-size:11.5px;color:#666;margin:10px 0 3px}
.item p{font-size:9.6px;line-height:13px;color:#666}
.item a{display:block;margin-top:4px;font-size:11px;color:var(--red);text-decoration:none}
.widget{top:844px;width:230px;height:154px;padding:9px 15px}
.widget .h2{padding-bottom:7px;border-bottom:1px solid #e4e4e4;display:block}
.video{margin-top:6px;width:197px;height:103px;position:relative;background:linear-gradient(#7a8a6a,#9aa88c 45%,#4d5b3a)}
.vbar{position:absolute;left:0;bottom:0;width:100%;height:15px;background:#222}
.play{position:absolute;left:85px;top:30px;width:27px;height:27px;border-radius:50%;background:var(--red);border:2px solid #fff}
.widget .small{font-size:9.2px;line-height:15px;color:#666;margin-top:11px}
.email{margin-top:10px;width:199px;height:27px;border:1px solid #ccc;background:#fff;font-size:9.5px;color:#999;padding:7px 10px}
.btn{margin-top:9px;width:54px;height:23px;background:var(--red);color:#fff;font-size:11px;display:flex;align-items:center;justify-content:center}
.quote{font-size:9.2px;line-height:15px;color:#666;margin-top:10px;padding-left:8px}
.quote b{font-family:"Open Sans",sans-serif;font-size:11px;color:#555;display:block;margin-top:3px}
.badge{position:absolute;top:1038px;background:#2a2a2a}
.follow{left:632px;top:1027px;width:230px;height:70px;text-align:center;padding-top:6px}
.social{display:flex;justify-content:center;gap:27px;margin-top:9px}
.social i{width:26px;height:26px;border-radius:3px}
.footer{left:0;top:1138px;width:984px;height:62px;background:var(--footer);color:#eee;font-size:9.5px;text-align:center;padding-top:15px}
.footer p{word-spacing:1px}
.footer span{margin:0 9px}
</style>
</head>
<body>

<div class="abs brand"><i class="brand-mark"></i>FELM Auction Group</div>

<div class="abs phone">
  <svg width="26" height="26" viewBox="0 0 26 26"><circle cx="13" cy="13" r="11.5" fill="none" stroke="#d0121a" stroke-width="2"/><path d="M9 7c1 0 2 2 2.3 3 .2.8-1 1.3-1 2 .4 1.4 2 3 3.4 3.5.7 0 1.2-1.2 2-1 1 .3 3 1.3 3 2.3 0 1.3-1.6 2.2-3 2.2-3.8 0-8.7-4.9-8.7-8.7C7 8.6 7.8 7 9 7z" fill="#d0121a"/></svg>
  270-555-0148
</div>

<nav class="abs nav">
  <a class="home" href="#" aria-label="Home"><svg width="16" height="15" viewBox="0 0 16 15"><path d="M8 1 1 7.5h2V14h4v-4h2v4h4V7.5h2z" fill="#fff"/></svg></a>
  <a href="#" style="width:131px">AUCTIONS</a>
  <a href="#" style="width:109px">SERVICES</a>
  <a href="#" style="width:109px">ABOUT US</a>
  <a href="#" style="width:80px">FAQs</a>
  <a href="#" style="width:130px">REFERENCES</a>
  <a href="#" style="width:118px">CONTACT US</a>
</nav>

<section class="abs slider">
  <div class="abs slide-photo" role="img" aria-label="Two-storey cream house with dark roof and glass veranda, surrounded by garden and trees"></div>
  <div class="abs cap cap-1">We provide the highest value for</div>
  <div class="abs cap cap-2">your home through Auction</div>
  <div class="abs dots"><i></i><i></i><i></i><i></i></div>
</section>

<section class="abs panel welcome">
  <h1>Welcome to <span>FELM AUCTION GROUP</span></h1>
  <p>Lorem ipsum dolor sit amet, consectetuer adipiscing elit, sed diam nonummy nibh euismod tincidunt ut laoreet dolore magna aliquam erat volutpat. Ut wisi enim ad minim veniam, quis nostrud exerci tation ullamcorper suscipit lobortis nisl ut aliquip ex ea commodo consequat. Duis autem vel eum iriure dolor in hendrerit in vulputate velit esse molestie consequat, vel illum dolore eu feugiat nulla facilisis at vero eros et accumsan et iusto odio dignissim qui blandit praesent luptatum zzril delenit augue duis dolore te feugait nulla facilisi.</p>
  <p>Ut wisi enim ad minim veniam, quis nostruexerci tation ullamcorper suscipit lobortis nisl ut aliquip accumsan et iusto odio dignissim qui blandit luptatum zzril delenit augue duis <span class="more">Read More</span></p>
</section>

<section class="abs panel featured">
  <span class="h2">Featured Auctions</span>
  <span class="arrow" style="left:6px;top:66px">&#8249;</span>
  <span class="arrow" style="left:720px;top:66px;color:#555">&#8250;</span>
  <div class="item" style="left:32px"><div class="thumb"><div role="img" aria-label="White colonial mansion on a lawn" style="background:linear-gradient(#6fa3e0,#e6e8ea 55%,#5f9a3c)"></div></div><h3>Lorem Ispum</h3><p>Lorem ipsum dolor sit amet, cdsfnsectetuer adipisdfcing elit, sed</p><a href="#">Read More</a></div>
  <div class="item" style="left:171px"><div class="thumb"><div role="img" aria-label="Modern house lit at dusk" style="background:linear-gradient(#3a4250,#8a5a3a 55%,#d98a3a)"></div></div><h3>Lorem Ispum</h3><p>Lorem ipsum dolor sit amet, cdsfnsectetuer adipisdfcing elit, sed</p><a href="#">Read More</a></div>
  <div class="item" style="left:310px"><div class="thumb"><div role="img" aria-label="Stone house with turret and garden" style="background:linear-gradient(#b8c6cc,#8c8f8a 55%,#3f7a2a)"></div></div><h3>Lorem Ispum</h3><p>Lorem ipsum dolor sit amet, cdsfnsectetuer adipisdfcing elit, sed</p><a href="#">Read More</a></div>
  <div class="item" style="left:449px"><div class="thumb"><div role="img" aria-label="Villa with palm trees at evening" style="background:linear-gradient(#5a5f6a,#9a7450 55%,#6a5a40)"></div></div><h3>Lorem Ispum</h3><p>Lorem ipsum dolor sit amet, cdsfnsectetuer adipisdfcing elit, sed</p><a href="#">Read More</a></div>
  <div class="item" style="left:587px"><div class="thumb"><div role="img" aria-label="Suburban house with garage" style="background:linear-gradient(#7ab0e6,#9a9a9e 55%,#5a8a3a)"></div></div><h3>Lorem Ispum</h3><p>Lorem ipsum dolor sit amet, cdsfnsectetuer adipisdfcing elit, sed</p><a href="#">Read More</a></div>
</section>

<section class="abs panel widget" style="left:123px">
  <span class="h2">Featured Video</span>
  <div class="video" role="img" aria-label="Video still of a house auction with crowd on the lawn">
    <div class="play"><svg width="23" height="23" viewBox="0 0 23 23"><path d="M9 6.5v10l8-5z" fill="#fff"/></svg></div>
    <div class="vbar"></div>
  </div>
</section>

<section class="abs panel widget" style="left:377px">
  <span class="h2">Subscribe to Newsletter</span>
  <p class="small">Newsletter to Keep up with the latest in getting the most out of your web presence.</p>
  <div class="email">Enter Your Email</div>
  <div class="btn">Signup</div>
</section>

<section class="abs panel widget" style="left:632px">
  <span class="h2">Testimonials</span>
  <span class="abs" style="right:16px;top:12px;font-size:13px;color:#777">&#8249;&nbsp;&nbsp;<b style="color:#333">&#8250;</b></span>
  <div class="quote"><span style="font-size:18px;color:#999;font-family:Georgia,serif;line-height:0">&ldquo;</span> Eenim ad minim veniam, quis nostrud exerc ullamcade orper suscipit lobortis nisl ut aliquip ex ea commodo consequat. Duis autem vel eum. Lorem ispum is the dummpy text of the insustry.<b>Dana Whitfield</b></div>
</section>

<span class="abs" style="left:129px;top:1044px;font-size:22px;color:#999">&#8249;</span>
<div class="badge" style="left:160px;width:52px;height:58px;border-radius:3px" role="img" aria-label="Partner badge"></div>
<div class="badge" style="left:255px;width:112px;height:52px;border-radius:50%;top:1041px" role="img" aria-label="Association badge"></div>
<div class="badge" style="left:410px;width:68px;height:58px;border-radius:50%" role="img" aria-label="Auctioneer certification badge"></div>
<div class="badge" style="left:524px;width:60px;height:62px;border-radius:3px;top:1036px" role="img" aria-label="Business membership badge"></div>
<span class="abs" style="left:604px;top:1044px;font-size:22px;color:#555">&#8250;</span>

<section class="abs panel follow">
  <span class="h2">Follow Us On</span>
  <div class="social">
    <i style="background:#3b5b9a" role="img" aria-label="Social profile 1"></i>
    <i style="background:#41a9e6" role="img" aria-label="Social profile 2"></i>
    <i style="background:#c8241f" role="img" aria-label="Social profile 3"></i>
  </div>
</section>

<footer class="abs footer">
  <p><span>4172 Quill Ferry Lane, Paducah, KY 42917</span><span>Toll Free: 1-800-555-BIDS (2437)</span><span>Phone: 270-555-0148</span><span>Fax: 270-555-0193</span></p>
  <p style="margin-top:10px">Copyright &copy; 2014.&nbsp; FELM Auction Group.&nbsp; All Rights Reserved.</p>
</footer>

</body>
</html>
```